Tarrowind High School Association Website New Design

We require a fresh new website design for the Tarrowind High School Old Boys Association. The association is a non-for-profit and as such we like the site to reflect the ethos.
We require a design that uses responsive design techniques, so to allow the site to shift between mobile, tablet and desktop spaces and maintain elements in the site.
We would like a landing/home page design, and also an inner news/article based design included.
We want the site to appeal to a broad market of both the old guard members but also to bring on board the new social savey younger members.
The site needs to have a modern take on a professional yet fresh and opulent/elegant look.
A site that we like influences from is http://www.quennaval-lodge.com/ we especially like the navigation look and feel.
The site needs to be clean and simple to find information and navigate and as such would like the site design elements to reflect this in its layout and element interplay.
This site will act as an information gateway for the member's, but also offer abilities to purchase memberships, get information on up coming events and purchase tickets to these events, and interact with the members on the site.
Hi All designers,
The client has now agreed to make the project funding guaranteed, so I hope to see some great designs from you.
Thanks
Sorry all, I hadn't uploaded the logo, has now been uploaded.
Hi all designers, please don't let the wireframe layout include restrict your design freedom on the page layout. We included this to give you a feel for the elements wanted in the site, but not to push you to have them all in that arrangement. Feel free to move around or remove parts of to make better use of the space.
Also this site is for ex-students who are members of an association linked to the school, and not for the school itself, so your designs need to lean towards a member, events and reunions type site design.
After a review today, client now requires that the sites Events need special consideration. Want to see in a prominent position on the landing page area a good area to showcase the upcoming events. Please take this into consideration in your future design layouts.
Hi All Designers, I appreciate all the new and current designs, and sorry a bit behind on the feedback, have been a bit swamped on my own workload, I will give feedback to you all, and will maybe look at an extension of the deadline if need be, as to also allow the clients to look over designs.
Thanks
Reason: Extending the project deadline to allow more feedback to be provider to all designers, to allow review by clients and the feedback through myself.
Reason: Client was un-available for comment, and want them to be able to give feedback to designers for last round updates.
Reason: Sorry all, client has been overseas, and will only be back next week, so need to extend the deadline to allow for client input next week.
Reason: Sorry client has be delayed overseas, so when be needing to work through the designs next week to allow full ability to give all designs due recognition.
Reason: Waiting for client to review designs.
Target Market(s)
Professionals from all varity of job types
Industry/Entity Type
Events
Requirements
Must have
- Please use the attached Logo in the design and look to use the current colour pallet as much as possible, but open to colour and pallet additions or amendments.
Must have a “hero” header image scroller for ability to showcase upcoming events and other items (Required for home/landing pages, could be amended or removed on inner pages).
Should look to follow the include wire frame layout concept as a good conception starting point - but do not limit to just this layout, use design discretion.
Include prominently positioned events area in layout for upcoming events to push the events heavy aspect of the site.
Should include icons/link abilities to access social sites and applications. Ie Plumvine etc.
Nice to have
- A modern look with an edge to it.
Creative use of the sites colour pallet and site elements.
Should not have
- should not be a copy of the wireframe with colour added

```html
<!DOCTYPE html>
<html lang="en">
<head>
<meta charset="utf-8">
<title>Tarrowind High School Old Boys Association</title>
<link rel="stylesheet" href="https://fonts.googleapis.com/css2?family=Roboto+Condensed:wght@300;400&family=Arimo:wght@400&family=Roboto:wght@400&display=swap">
<style>
:root{
  --page:#ebebeb;
  --white:#ffffff;
  --ink:#222222;
  --text:#333333;
  --line:#cccccc;
  --green:#0c6b3c;
  --green-dark:#07512c;
  --green-light:#2ba86a;
  --brand:#23201f;
  --slide-sky:#a9c6e3;
  --slide-brick:#7a3a2e;
  --slide-grass:#5f8a3a;
}
*{box-sizing:border-box;margin:0;padding:0}
html,body{width:800px;height:1200px;overflow:hidden}
body{background:var(--page);position:relative;font-family:"Arimo",Arial,sans-serif;color:var(--text)}
.heading{font-family:"Roboto Condensed",Arial,sans-serif;font-weight:300;color:var(--ink)}

/* header */
.site-header{position:absolute;left:0;top:0;width:800px;height:88px}
.brand{position:absolute;left:58px;top:20px;display:flex;align-items:center;gap:10px}
.brand-mark{width:14px;height:14px;background:var(--green)}
.brand-name{font-family:"Roboto Condensed",Arial,sans-serif;font-weight:400;font-size:42px;line-height:46px;color:var(--brand)}
.social-top{position:absolute;right:58px;top:11px;display:flex;gap:9px}
.social-square{width:26px;height:26px;border-radius:4px}
.sq-plumvine{background:#3b5a98}
.sq-chirpwell{background:#4cb3e0}
.sq-feed{background:#f08a24}
.search{position:absolute;right:57px;top:47px;width:219px;height:24px;border:1px solid #b9b9b9;border-radius:6px;background:var(--white);font-size:12px;color:#555;padding:4px 8px;display:flex;justify-content:space-between;align-items:center}

/* navigation */
.main-nav{position:absolute;left:0;top:88px;width:800px;height:39px;background:linear-gradient(#1a8a52,var(--green) 50%,var(--green-dark));border-top:2px solid #b9d7c5;border-bottom:3px solid #0a5a32}
.main-nav ul{list-style:none;display:flex;position:absolute;left:58px;top:0;height:34px}
.main-nav li{font-family:"Roboto Condensed",Arial,sans-serif;font-size:13px;color:var(--white);display:flex;align-items:center;justify-content:center;height:34px;border-left:1px solid rgba(255,255,255,.15)}
.main-nav li:first-child{border-left:0}
.main-nav li.active{background:var(--green-light);border-radius:3px 3px 0 0}

/* hero */
.hero{position:absolute;left:58px;top:141px;width:684px;height:288px;background:var(--white);border:1px solid #cfcfcf;box-shadow:0 1px 4px rgba(0,0,0,.25)}
.hero-image{width:682px;height:251px;background:linear-gradient(var(--slide-sky) 0%,#dfe9f2 22%,var(--slide-brick) 30%,#6a3a31 55%,var(--slide-grass) 68%,#4d7a2f 85%,#7ea353 100%)}
.hero-caption{height:35px;display:flex;align-items:center;justify-content:center;font-size:19px;position:relative}
.hero-dots{position:absolute;right:12px;top:13px;display:flex;gap:5px}
.hero-dots span{width:9px;height:9px;border-radius:50%;background:#999}
.hero-dots span:first-child{background:var(--green-dark)}
.hero-arrow{position:absolute;top:248px;width:24px;height:24px;border-radius:50%;background:#d6d6d6;display:flex;align-items:center;justify-content:center}

/* intro */
.intro{position:absolute;left:0;top:454px;width:800px;height:236px;background:var(--white)}
.intro-col{position:absolute;top:11px;height:215px}
.col-who{left:58px;width:204px}
.col-what{left:300px;width:182px}
.col-how{left:520px;width:222px}
.divider{position:absolute;top:11px;width:1px;height:215px;background:var(--line)}
.intro-col h2{font-size:19px;margin:9px 0 0}
.intro-col p{position:absolute;top:55px;left:0;right:0;font-size:8.3px;line-height:13.8px;text-align:justify}
.col-how p{top:52px}
.intro-col .btn{position:absolute;top:176px;left:0}
.btn{display:inline-flex;align-items:center;justify-content:center;width:60px;height:25px;border-radius:5px;background:linear-gradient(#16844d,var(--green-dark));color:var(--white);font-family:"Roboto Condensed",Arial,sans-serif;font-weight:300;font-size:16px}

/* panels */
.panel{position:absolute;top:721px;height:251px;background:var(--white);border:1px solid #c4c4c4;border-radius:6px;overflow:hidden}
.panel-title{height:31px;background:linear-gradient(#1a8a52,var(--green-dark));color:var(--white);font-size:16px;padding:6px 19px;font-family:"Roboto Condensed",Arial,sans-serif;font-weight:300}
.events{left:58px;width:456px}
.event-list{display:flex;gap:32px;padding:16px 20px 0}
.event{width:117px}
.event-photo{width:117px;height:108px}
.ev1{background:linear-gradient(#5a3a2a,#1c1410)}
.ev2{background:linear-gradient(#1d1f3a,#4b3f5a 60%,#d9d9e6)}
.ev3{background:linear-gradient(#2a3d7a,#5c5f8e 55%,#b7a888)}
.event h3{font-family:"Roboto",Arial,sans-serif;font-weight:400;color:var(--green);font-size:16px;margin:14px 0 7px;white-space:nowrap}
.event p{font-size:8.6px;line-height:11px;color:var(--ink)}
.gallery{left:533px;width:210px}
.gallery-photo{width:184px;height:190px;margin:13px 0 0 13px;background:linear-gradient(#4a6a5a,#2a2a22 45%,#6b4a2c)}

/* footer */
.site-footer{position:absolute;left:58px;top:997px;width:685px;height:203px;background:var(--white);display:flex;padding-top:14px}
.foot-col{height:189px}
.foot-col h2{font-size:16px;margin-bottom:12px}
.quick{width:225px;padding-left:17px;border-right:1px solid var(--line)}
.quick ul{list-style:none;display:grid;grid-template-columns:101px 100px;row-gap:8px;font-size:8.6px;color:var(--ink)}
.quick li::before{content:"›";font-weight:bold;margin-right:6px}
.contact{width:222px;padding-left:17px;border-right:1px solid var(--line)}
.contact p{font-size:11.5px;line-height:21.5px;color:var(--ink)}
.social{padding-left:20px;width:236px}
.social-row{display:flex;gap:9px;margin-bottom:17px}
.email{width:200px;height:24px;border:1px solid #bbb;border-radius:6px;font-size:9px;padding:6px 10px;color:var(--ink);margin-bottom:13px;box-shadow:inset 0 1px 2px rgba(0,0,0,.1)}
</style>
</head>
<body>
<header class="site-header">
  <div class="brand"><span class="brand-mark"></span><span class="brand-name">Tarrowind Old Boys</span></div>
  <div class="social-top">
    <span class="social-square sq-plumvine" role="img" aria-label="Plumvine"></span>
    <span class="social-square sq-chirpwell" role="img" aria-label="Chirpwell"></span>
    <span class="social-square sq-feed" role="img" aria-label="News feed"></span>
  </div>
  <div class="search"><span>Search</span>
    <svg width="10" height="10" viewBox="0 0 10 10"><circle cx="6" cy="4" r="3" fill="none" stroke="#3a9a3a" stroke-width="1.4"/><line x1="4" y1="6" x2="1" y2="9" stroke="#3a9a3a" stroke-width="1.6"/></svg>
  </div>
</header>

<nav class="main-nav">
  <ul>
    <li class="active" style="width:57px">HOME</li>
    <li style="width:142px">NEWS</li>
    <li style="width:120px">EVENTS</li>
    <li style="width:121px">PHOTOS</li>
    <li style="width:137px">MEMBERSHIP</li>
    <li style="width:111px">CONTACT</li>
  </ul>
</nav>

<span class="hero-arrow" style="left:13px"><svg width="8" height="8" viewBox="0 0 8 8"><path d="M5 1 L2 4 L5 7" fill="none" stroke="#666" stroke-width="1.3"/></svg></span>
<span class="hero-arrow" style="left:758px"><svg width="8" height="8" viewBox="0 0 8 8"><path d="M3 1 L6 4 L3 7" fill="none" stroke="#666" stroke-width="1.3"/></svg></span>
<section class="hero">
  <div class="hero-image" role="img" aria-label="Photo of the school's brick building with towers above a grassy hill and car park"></div>
  <div class="hero-caption heading">“The Association Of Excellence”
    <div class="hero-dots"><span></span><span></span><span></span><span></span></div>
  </div>
</section>

<section class="intro">
  <article class="intro-col col-who">
    <h2 class="heading">Who We Are</h2>
    <p>Lorem Ipsum is simply dummy text of the printing and typesetting industry. Lorem Ipsum has been the industry's standard dummy text ever since the 1500s, when an unknown printer took a galley of type and scrambled it to make a type specimen book. It has survived not only five centuries, but also the leap into electronic typesetting, remaining essentially unchanged. versions of Lorem Ipsum.</p>
    <span class="btn">More</span>
  </article>
  <span class="divider" style="left:280px"></span>
  <article class="intro-col col-what">
    <h2 class="heading">What We Do</h2>
    <p>Lorem Ipsum is simply dummy text of the printing and typesetting industry. Lorem Ipsum has been the industry's standard dummy text ever since the 1500s, when an unknown printer took a galley of type and scrambled it to make a type specimen book. It has survived not only five centuries, but also the leap into electronic typesetting, remaining essentially unchanged. versions of Lorem Ipsum.</p>
    <span class="btn">More</span>
  </article>
  <span class="divider" style="left:499px"></span>
  <article class="intro-col col-how">
    <h2 class="heading">How we do it</h2>
    <p>Lorem Ipsum is simply dummy text of the printing and typesetting industry. Lorem Ipsum has been the industry's standard dummy text ever since the 1500s, when an unknown printer took a galley of type and scrambled it to make a type specimen book. It has survived not only five centuries, but also the leap into electronic typesetting, remaining essentially unchanged. versions of Lorem Ipsum remaining essentially unchanged. versions of Lorem Ipsum.</p>
    <span class="btn">More</span>
  </article>
</section>

<section class="panel events">
  <h2 class="panel-title">Upcoming Events</h2>
  <div class="event-list">
    <div class="event">
      <div class="event-photo ev1" role="img" aria-label="School band performing in a hall"></div>
      <h3>Event Name</h3>
      <p>Lorem Ipsum is simply dummy text of the printing and typesetting industry.</p>
    </div>
    <div class="event">
      <div class="event-photo ev2" role="img" aria-label="Decorated ballroom set for a formal dinner"></div>
      <h3>Event Name</h3>
      <p>Lorem Ipsum is simply dummy text of the printing and typesetting industry.</p>
    </div>
    <div class="event">
      <div class="event-photo ev3" role="img" aria-label="Conference hall with round tables and screens"></div>
      <h3>Event Name</h3>
      <p>Lorem Ipsum is simply dummy text of the printing and typesetting industry.</p>
    </div>
  </div>
</section>

<section class="panel gallery">
  <h2 class="panel-title">Photo gallery</h2>
  <div class="gallery-photo" role="img" aria-label="Band playing under a glass atrium roof"></div>
</section>

<footer class="site-footer">
  <div class="foot-col quick">
    <h2 class="heading">Quick Links</h2>
    <ul>
      <li>Payments</li><li>Payments</li>
      <li>About Us</li><li>About Us</li>
      <li>Contact Us</li><li>Contact Us</li>
      <li>Links</li><li>Links</li>
    </ul>
  </div>
  <div class="foot-col contact">
    <h2 class="heading">Contact Us</h2>
    <p>(03) 5550 1842</p>
    <p>info@emailtogohere.com</p>
    <p>www.yoursitehere.com</p>
    <p>53, your street to go here</p>
  </div>
  <div class="foot-col social">
    <h2 class="heading">Get Social</h2>
    <div class="social-row">
      <span class="social-square sq-plumvine" role="img" aria-label="Plumvine"></span>
      <span class="social-square sq-chirpwell" role="img" aria-label="Chirpwell"></span>
      <span class="social-square sq-feed" role="img" aria-label="News feed"></span>
    </div>
    <div class="email">Enter Email Address</div>
    <span class="btn">Join</span>
  </div>
</footer>
</body>
</html>
```